Verdant Solutions Business Card

want the back of card to be blue- with the logo in the center
front of card- info plus logo (info being mailing address, email address, and website address )
4 different names with titles to have on cards
1) Dalton Mirsky - Owner
2) Brenda Tolvin- Customer Relationship Specialist
3) Henri Kastner- Vice President of Sales
4) Wade Dunmor- Chief Technology Officer

Target Market(s)

tech company in the government/probation office industry

Industry/Entity Type

Government Office

Contact Information for Business Card

1) Dalton Mirsky - Owner

Colors
0355a3
ffffff

Requirements
Must have
• back side should be blue, with the logo placed in the center
• front side needs to include both the logo, as well as company info (info should include website address, email address, and mailing address)

```html
<!DOCTYPE html>
<html lang="en">
<head>
<meta charset="utf-8">
<title>Verdant Solutions Business Card</title>
<link href="https://fonts.googleapis.com/css2?family=Cinzel:wght@400;600&family=Open+Sans:wght@400;600&display=swap" rel="stylesheet">
<style>
  :root {
    --navy: #1c3563;
    --navy-deep: #16294f;
    --navy-light: #2f4a7c;
    --paper: #ffffff;
    --paper-shade: #ececec;
    --ink: #555a63;
    --ink-soft: #6b6f76;
    --stage: #e9eaec;
  }
  * { box-sizing: border-box; margin: 0; padding: 0; }
  html, body {
    width: 1200px;
    height: 900px;
    overflow: hidden;
    background: var(--stage);
  }
  .stage {
    width: 1200px;
    height: 900px;
    display: flex;
    flex-direction: column;
    align-items: center;
    justify-content: center;
    gap: 40px;
  }
  .card {
    width: 630px;
    height: 360px;
    position: relative;
    box-shadow: 0 6px 18px rgba(0, 0, 0, 0.18);
  }

  /* Back side */
  .card-back {
    background: linear-gradient(120deg, var(--navy-deep) 0%, var(--navy) 55%, var(--navy-light) 100%);
    display: flex;
    align-items: center;
    justify-content: center;
  }
  .wordmark {
    font-family: "Cinzel", serif;
    font-weight: 600;
    letter-spacing: 1px;
    line-height: 1;
    white-space: nowrap;
  }
  .card-back .wordmark {
    color: var(--paper);
    font-size: 40px;
  }

  /* Front side */
  .card-front {
    background: linear-gradient(135deg, var(--paper) 0%, var(--paper) 45%, var(--paper-shade) 100%);
    display: flex;
    align-items: center;
    padding: 0 36px 0 40px;
  }
  .front-brand {
    width: 240px;
    flex: none;
    display: flex;
    justify-content: center;
  }
  .card-front .wordmark {
    color: var(--navy);
    font-size: 28px;
    text-align: center;
    line-height: 1.15;
  }
  .wordmark-line {
    display: block;
  }
  .divider {
    width: 2px;
    height: 170px;
    flex: none;
    background: var(--navy);
    margin: 0 28px 0 24px;
  }
  .details {
    display: flex;
    flex-direction: column;
    min-width: 0;
  }
  .person-name {
    font-family: "Cinzel", serif;
    font-weight: 400;
    font-size: 25px;
    color: var(--ink);
    letter-spacing: 1px;
    line-height: 1;
    white-space: nowrap;
  }
  .person-title {
    font-family: "Open Sans", sans-serif;
    font-weight: 600;
    font-size: 13px;
    color: var(--navy);
    margin-top: 2px;
    margin-bottom: 18px;
  }
  .contact-list {
    list-style: none;
    display: flex;
    flex-direction: column;
    gap: 6px;
  }
  .contact-item {
    display: flex;
    align-items: center;
    gap: 10px;
    font-family: "Open Sans", sans-serif;
    font-size: 15px;
    color: var(--ink-soft);
  }
  .contact-icon {
    width: 14px;
    height: 14px;
    flex: none;
  }
  .address {
    font-family: "Open Sans", sans-serif;
    font-size: 15px;
    color: var(--ink-soft);
    margin-top: 10px;
  }
</style>
</head>
<body>
<main class="stage">
  <section class="card card-back" aria-label="Card back">
    <span class="wordmark">VERDANT SOLUTIONS</span>
  </section>

  <section class="card card-front" aria-label="Card front">
    <div class="front-brand">
      <span class="wordmark">
        <span class="wordmark-line">VERDANT</span>
        <span class="wordmark-line">SOLUTIONS</span>
      </span>
    </div>
    <div class="divider"></div>
    <div class="details">
      <p class="person-name">DALTON MIRSKY</p>
      <p class="person-title">Owner</p>
      <ul class="contact-list">
        <li class="contact-item">
          <svg class="contact-icon" viewBox="0 0 24 24" aria-hidden="true">
            <path fill="#3a3f48" d="M6.6 10.8c1.4 2.8 3.8 5.1 6.6 6.6l2.2-2.2c.3-.3.7-.4 1-.2 1.1.4 2.3.6 3.6.6.6 0 1 .4 1 1V20c0 .6-.4 1-1 1C10.6 21 3 13.4 3 4c0-.6.4-1 1-1h3.5c.6 0 1 .4 1 1 0 1.3.2 2.5.6 3.6.1.3 0 .7-.2 1z"/>
          </svg>
          <span>000 000 0000</span>
        </li>
        <li class="contact-item">
          <svg class="contact-icon" viewBox="0 0 24 24" aria-hidden="true">
            <rect x="2" y="5" width="20" height="14" rx="1" fill="#1c3563"/>
            <path d="M2.5 5.5 12 13l9.5-7.5" fill="none" stroke="#ffffff" stroke-width="1.6"/>
          </svg>
          <span>youremail@xyz.com</span>
        </li>
        <li class="contact-item">
          <svg class="contact-icon" viewBox="0 0 24 24" aria-hidden="true">
            <g fill="none" stroke="#3a3f48" stroke-width="1.8">
              <circle cx="12" cy="12" r="9.5"/>
              <ellipse cx="12" cy="12" rx="4.2" ry="9.5"/>
              <path d="M2.5 12h19M4 7h16M4 17h16"/>
            </g>
          </svg>
          <span>www.yourwebsite.com</span>
        </li>
      </ul>
      <p class="address">Your Address here</p>
    </div>
  </section>
</main>
</body>
</html>
```